Medical equipment business looking for professional, unique business card

We need a business card design for a durable medical equipment company. We are small but would like our cards to express that we are much bigger. We focus on braces (back, knee, wrist, etc) but also do crutches, rollators, wheelchairs- basically medical equipment that gets you going and back in Action. Our colors are blue and green and our logo has an arrow and use of a "spine". We'd like to express professionalism while being unique.

Industry/Entity Type

Medical Equipment

Contact Information for Business Card

Professional feel but unique. Memorable.

Font styles to use
Serif
Sans Serif
Other font styles liked:
• verdana

Requirements
Must have
• card holders cell#, business phone#, fax#, email, website address, business address, logo
Nice to have
• use of medical/healthcare related descriptive words, items, look
Should not have
• the wrong colors or cartoon characters.

```html
<!DOCTYPE html>
<html lang="en">
<head>
<meta charset="utf-8">
<title>Rennvale – Business Card</title>
<link rel="stylesheet" href="https://fonts.googleapis.com/css2?family=Open+Sans:ital,wght@0,400;0,600;0,700;1,700&display=swap">
<style>
  :root {
    --navy: #0b4268;
    --green: #8cc43f;
    --sky: #1e8bc3;
    --white: #ffffff;
    --stage: #e9ecef;
  }
  * { margin: 0; padding: 0; box-sizing: border-box; }
  html, body { width: 1200px; height: 900px; overflow: hidden; }
  body {
    background: var(--stage);
    font-family: "Open Sans", Arial, sans-serif;
    position: relative;
  }
  .card {
    position: absolute;
    overflow: hidden;
    box-shadow: 0 6px 18px rgba(0,0,0,.18);
  }
  .card-front { left: 77px; top: 33px; width: 590px; height: 365px; background: var(--white); }
  .card-back { left: 388px; top: 505px; width: 567px; height: 352px; background: var(--navy); }
  .front-bands { position: absolute; left: 0; top: 0; width: 590px; height: 365px; }

  .brand { position: absolute; text-align: center; }
  .brand-front { left: 0; width: 590px; top: 50px; }
  .brand-back { left: 0; width: 567px; top: 134px; }
  .brand-name {
    display: inline-flex; align-items: center; gap: 10px;
    font-weight: 600; font-size: 46px; line-height: 1; letter-spacing: -0.5px;
  }
  .brand-front .brand-name { color: var(--navy); }
  .brand-back .brand-name { color: var(--white); }
  .brand-dot { width: 14px; height: 14px; border-radius: 50%; background: var(--green); }
  .brand-tagline { font-weight: 600; }
  .brand-front .brand-tagline { margin-top: 16px; font-size: 15px; color: var(--sky); }
  .brand-back .brand-tagline { margin-top: 20px; font-size: 16px; color: var(--white); }

  .contact-list {
    position: absolute; left: 35px; top: 250px;
    list-style: none; color: var(--white); font-size: 15px; line-height: 21px;
  }
  .contact-list li { display: flex; align-items: center; gap: 6px; }
  .contact-list svg { width: 12px; height: 12px; fill: var(--white); flex: none; }

  .holder {
    position: absolute; right: 38px; top: 237px; text-align: right; color: var(--white);
  }
  .holder-name { font-size: 19px; font-weight: 700; line-height: 24px; }
  .holder-title { font-size: 15px; line-height: 20px; }
  .holder-address { margin-top: 9px; font-size: 15px; line-height: 21px; font-style: normal; }

  .website {
    position: absolute; left: 198px; top: 277px;
    color: var(--green); font-size: 14px; font-weight: 700; font-style: italic;
  }
</style>
</head>
<body>

<section class="card card-front">
  <svg class="front-bands" viewBox="0 0 590 365" aria-hidden="true">
    <polygon points="0,190 402,190 380,217 0,217" fill="var(--green)"/>
    <polygon points="0,217 386,217 416,180 590,180 590,365 0,365" fill="var(--navy)"/>
  </svg>

  <div class="brand brand-front">
    <div class="brand-name"><span class="brand-dot"></span>Rennvale</div>
    <div class="brand-tagline">Durable Medical Equipment</div>
  </div>

  <ul class="contact-list">
    <li><svg viewBox="0 0 12 12"><path d="M2.5 0.5l2 2.2-1 1.3c.7 1.6 1.9 2.8 3.5 3.5l1.3-1 2.2 2-1 2.5C5 10.8 1.2 7 0 1.5z"/></svg>044-555 010 200</li>
    <li><svg viewBox="0 0 12 12"><rect x="2" y="0.5" width="8" height="3.5"/><rect x="0.5" y="4.5" width="11" height="5.5" rx="1"/><rect x="2.5" y="8" width="7" height="3.5" fill="var(--navy)" stroke="var(--white)"/></svg>044-555 010 201</li>
    <li><svg viewBox="0 0 12 12"><rect x="3" y="0" width="6" height="12" rx="1"/><rect x="4" y="1.5" width="4" height="7.5" fill="var(--navy)"/></svg>044-555 010 202</li>
    <li><svg viewBox="0 0 12 12"><rect x="0.5" y="2" width="11" height="8"/><path d="M0.5 2.5L6 6.5l5.5-4" fill="none" stroke="var(--navy)" stroke-width="1.2"/></svg>hello@rennvale.com</li>
  </ul>

  <div class="holder">
    <div class="holder-name">Daniel Porter</div>
    <div class="holder-title">Managing Director</div>
    <address class="holder-address">48 Harbour Road<br>Westbridge, 204518.</address>
  </div>
</section>

<section class="card card-back">
  <div class="brand brand-back">
    <div class="brand-name"><span class="brand-dot"></span>Rennvale</div>
    <div class="brand-tagline">Durable Medical Equipment</div>
  </div>
  <div class="website">www.rennvale.com</div>
</section>

</body>
</html>
```